All-natural soap packaging design for new company

The box type has been selected, we just need artwork for each of our 10 products. I'd like the same look to each, the idea is just to switch out the name and ingredient label on each. The dimensions are 3.5"x3.75"x1.25". The colors in the uploaded pictures with product titles are not mandatory. I'd like to keep the font on the packaging (Rubik) as it is the same as the website.

Target Market(s)

Health & Beauty, people looking for natural or organic products

Industry/Entity Type

It Company

Colors

Designer to choose colors to be used in the design.

Requirements
Must have
• Design must be clean and relatively simple. Slightly different look for each of the 10 products. Audience is people looking for all-natural products.

```html
<!DOCTYPE html>
<html lang="en">
<head>
<meta charset="UTF-8">
<title>Recipe No. 3 – Rosemary + Sweet Basil Soap Box Artwork</title>
<link href="https://fonts.googleapis.com/css2?family=Rubik:wght@300;400;500&display=swap" rel="stylesheet">
<style>
  :root {
    --canvas-bg: #d8d9da;
    --panel-white: #f2f2f2;
    --band-purple: #6a3f8f;
    --frame-pink: #cf86c9;
    --text-light: #f4eef7;
    --bubble-deep: #a94a9b;
    --bubble-mid: #c46cb8;
    --bubble-light: #e0a6d8;
    --herb-bloom: #7d55b0;
    --herb-stem: #6f9a4c;
    --brand-ink: #4a4a4c;
    --brand-blue: #2f7fc4;
  }
  * { margin: 0; padding: 0; box-sizing: border-box; }
  html, body {
    width: 1200px;
    height: 800px;
    overflow: hidden;
    background: var(--canvas-bg);
    font-family: "Rubik", sans-serif;
  }
  .artwork {
    position: relative;
    width: 1200px;
    height: 800px;
  }
  .lid-panel {
    position: absolute;
    left: 240px;
    top: 100px;
    width: 720px;
    height: 370px;
    background: var(--panel-white);
    overflow: hidden;
  }
  .herb-photo {
    position: absolute;
    left: 200px;
    top: 18px;
    width: 130px;
    height: 122px;
    background: linear-gradient(to bottom, var(--herb-bloom) 0%, #9a78c6 55%, var(--herb-stem) 80%, #89b262 100%);
    border-radius: 40px 40px 6px 6px;
  }
  .recipe-band {
    position: absolute;
    left: 0;
    top: 140px;
    width: 720px;
    height: 104px;
    background: var(--band-purple);
  }
  .recipe-band__frame {
    position: absolute;
    inset: 8px 10px;
    border: 1.5px solid var(--frame-pink);
  }
  .recipe-title,
  .side-title {
    position: absolute;
    color: var(--text-light);
    font-weight: 300;
    letter-spacing: 1.5px;
    line-height: 1.1;
    white-space: nowrap;
  }
  .recipe-title { left: 50px; top: 18px; }
  .side-title { left: 160px; top: 48px; }
  .recipe-title__number,
  .side-title__number { display: block; font-size: 27px; padding-left: 60px; }
  .recipe-title__name,
  .side-title__name { display: block; font-size: 36px; }
  .brand-mark {
    position: absolute;
    right: 40px;
    top: 262px;
    display: flex;
    align-items: center;
    gap: 12px;
  }
  .brand-mark__square {
    width: 24px;
    height: 24px;
    background: var(--brand-blue);
  }
  .brand-mark__name {
    font-weight: 500;
    font-size: 22px;
    letter-spacing: 1px;
    color: var(--brand-ink);
    text-transform: uppercase;
  }
  .side-panel {
    position: absolute;
    left: 240px;
    top: 490px;
    width: 720px;
    height: 190px;
    overflow: hidden;
  }
  .bubble-texture {
    position: absolute;
    inset: 0;
    background: linear-gradient(100deg, var(--bubble-mid) 0%, var(--bubble-light) 35%, var(--bubble-mid) 70%, var(--bubble-deep) 100%);
  }
</style>
</head>
<body>
  <main class="artwork">
    <section class="lid-panel">
      <div class="herb-photo" role="img" aria-label="Photograph of a bundled bunch of herb flowers"></div>
      <div class="recipe-band">
        <div class="recipe-band__frame"></div>
        <h1 class="recipe-title">
          <span class="recipe-title__number">RECIPE NO. 3</span>
          <span class="recipe-title__name">ROSEMARY + SWEET BASIL</span>
        </h1>
      </div>
      <div class="brand-mark">
        <span class="brand-mark__square"></span>
        <span class="brand-mark__name">Alder Soap Co.</span>
      </div>
    </section>
    <section class="side-panel">
      <div class="bubble-texture" role="img" aria-label="Close-up photograph of pink soap foam bubbles"></div>
      <h2 class="side-title">
        <span class="side-title__number">RECIPE NO. 3</span>
        <span class="side-title__name">ROSEMARY + SWEET BASIL</span>
      </h2>
    </section>
  </main>
</body>
</html>
```